Modern Business Card For A Digital Advertising Company

I'll be print on the Tarn Prints Velour paper http://us.tarnprints.example/products/velour/business-cards.html
Need's to be modern and use the color palette of the logo or gray scales. I think integrating the pixelation of the logo in to the card and having it wrap from one side to the other could be interesting. My company provides ad operations, web development, and number of other services to websites around the world. You can see my website at http://www.pixelharbor.example
Contact info on the card needs to have
Dana Welloby
President
p.555.318.4406
dana@pixelharbor.example
http://www.pixelharbor.example
Doesn't necessarily need to be in that order
Target Market(s)
Website owners
Industry/Entity Type
Business
Look and feel

```html
<!DOCTYPE html>
<html lang="en">
<head>
<meta charset="utf-8">
<title>Pixel Harbor – Business Card</title>
<link href="https://fonts.googleapis.com/css2?family=Ubuntu:wght@400;700&display=swap" rel="stylesheet">
<style>
  :root {
    --bg: #e9eaea;
    --green-light: #93c94a;
    --green: #7ab536;
    --green-dark: #5b9426;
    --band: #1b1b1b;
    --white: #ffffff;
    --text-light: #f2f2f2;
    --card-shadow: rgba(0, 0, 0, 0.18);
  }
  html, body {
    margin: 0;
    padding: 0;
    width: 1200px;
    height: 902px;
    overflow: hidden;
    background: var(--bg);
  }
  .canvas {
    position: relative;
    width: 1200px;
    height: 902px;
    display: flex;
    align-items: center;
    justify-content: center;
    gap: 40px;
  }
  .card {
    position: relative;
    width: 540px;
    height: 309px;
    box-shadow: 0 6px 18px var(--card-shadow);
    overflow: hidden;
    font-family: "Ubuntu", sans-serif;
  }
  .card--front {
    background: radial-gradient(ellipse at 50% 38%, var(--green-light) 0%, var(--green) 45%, var(--green-dark) 100%);
  }
  .identity {
    position: absolute;
    top: 98px;
    left: 0;
    right: 0;
    text-align: center;
  }
  .identity__name {
    display: inline-block;
    position: relative;
    margin: 0;
    font-size: 34px;
    font-weight: 700;
    color: var(--white);
    letter-spacing: 0.5px;
  }
  .identity__title {
    position: absolute;
    right: 0;
    bottom: -14px;
    font-size: 9px;
    font-weight: 700;
    letter-spacing: 1px;
    color: var(--white);
  }
  .contact-band {
    position: absolute;
    left: 0;
    right: 0;
    bottom: 16px;
    height: 30px;
    background: var(--band);
    display: flex;
    align-items: center;
    justify-content: space-between;
    padding: 0 14px;
    box-sizing: border-box;
  }
  .contact-item {
    display: flex;
    align-items: center;
    gap: 6px;
    font-size: 11px;
    color: var(--text-light);
  }
  .contact-item svg {
    width: 14px;
    height: 14px;
  }
  .card--back {
    background: var(--white);
    display: flex;
    align-items: center;
    justify-content: center;
  }
  .brand {
    display: flex;
    align-items: center;
    gap: 12px;
  }
  .brand__square {
    width: 26px;
    height: 26px;
    background: var(--green);
  }
  .brand__name {
    font-size: 30px;
    font-weight: 700;
    color: var(--green);
    letter-spacing: 1px;
  }
</style>
</head>
<body>
<main class="canvas">
  <section class="card card--front" aria-label="Business card front">
    <div class="identity">
      <h1 class="identity__name">Dana Welloby<span class="identity__title">PRESIDENT</span></h1>
    </div>
    <div class="contact-band">
      <div class="contact-item">
        <svg viewBox="0 0 14 14" aria-hidden="true"><circle cx="7" cy="7" r="7" fill="#e8b83a"/><rect x="3.5" y="4.5" width="7" height="5" fill="#fff"/><path d="M3.5 4.5 L7 7.5 L10.5 4.5" stroke="#e8b83a" fill="none" stroke-width="0.8"/></svg>
        <span>dana@pixelharbor.example</span>
      </div>
      <div class="contact-item">
        <svg viewBox="0 0 14 14" aria-hidden="true"><path d="M4 1.5 L6 4 L4.8 5.3 C5.5 7 7 8.5 8.7 9.2 L10 8 L12.5 10 L11 12.5 C6 12 2 8 1.5 3 Z" fill="#ffffff"/></svg>
        <span>555.318.4406</span>
      </div>
      <div class="contact-item">
        <svg viewBox="0 0 14 14" aria-hidden="true"><circle cx="7" cy="7" r="6.5" fill="#3c9bd6"/><path d="M3 5 Q5 3 7 4.5 Q6 7 4 7 Z M8 8 Q10 7 11 9 Q9.5 11.5 8 10.5 Z" fill="#7ac043"/></svg>
        <span>www.pixelharbor.example</span>
      </div>
    </div>
  </section>

  <section class="card card--back" aria-label="Business card back">
    <div class="brand">
      <span class="brand__square" aria-hidden="true"></span>
      <span class="brand__name">PIXEL HARBOR</span>
    </div>
  </section>
</main>
</body>
</html>
```